New College Graduate Resume - Creative and unique design that stands out from the rest

Need creative resume design for recent college graduate who graduated from School of Music with a concentration in music composition and production. Striving for a contemporary layout/design that allows the resume to "be unique" and "stand out" but be polished and professional. Open to integrating moderate color/graphics as part of resume design but the design can be minus those attributes as well. Attached is raw content in 7 sections (name/contact info, education, highlights of qualifications, work experience, honors/awards, and professional affiliations). While the designer has full latitude over overall design which (section headers, font type, separation/spacing, use of bullets, justification of text, etc.) please maintain current order/sequence of the 7 sections.

Industry/Entity Type

School

Requirements
Must have
• Name (Tobias Garrick Elwin III) should be most prominent (bold/font size) compared to remainder of resume copy.
• Section headers should be prominent but less so when compared to name on resume.
• The attached file of resume content is provided as raw source copy and is NOT to be just copied and pasted into open fields as is. Expectation is each section of copy will be organized in a manner that is most visually appealing and may include bullets, appropriate spacing, etc.
Should not have
• The attached file of resume content is provided as source copy and is NOT to be just copied and pasted into open fields as is. Expectation is each section of copy will be organized in a manner that

```html
<!DOCTYPE html>
<html lang="en">
<head>
<meta charset="utf-8">
<title>Tobias Garrick Elwin III – Resume</title>
<link href="https://fonts.googleapis.com/css2?family=Questrial&family=EB+Garamond:wght@400;500&family=Lato:wght@400;700&display=swap" rel="stylesheet">
<style>
:root{
  --bg:#ececec;
  --paper:#ffffff;
  --band:#eeefef;
  --blue:#2fb4ee;
  --grey-bar:#7a7a7a;
  --ink:#3a3a3a;
  --ink-soft:#555;
  --line:#4a4a4a;
}
*{box-sizing:border-box;margin:0;padding:0}
html,body{width:1200px;height:900px;overflow:hidden;background:var(--bg)}
body{font-family:"Lato",sans-serif;color:var(--ink);font-size:10px;line-height:1.32}
.resume{position:absolute;left:265px;top:10px;width:670px;height:880px;background:var(--paper);box-shadow:0 4px 18px rgba(0,0,0,.12);overflow:hidden;display:flex;flex-direction:column}
.top-bar{display:flex;height:20px;flex:none}
.top-bar .grey{flex:0 0 52%;background:var(--grey-bar)}
.top-bar .blue{flex:1;background:var(--blue)}
.masthead{height:84px;flex:none;background:var(--band);padding:14px 30px 0 22px}
.masthead-row{display:flex;align-items:flex-start;gap:14px}
.name{font-family:"Questrial",sans-serif;color:var(--blue);font-size:30px;line-height:1.1;letter-spacing:.5px;font-weight:400;white-space:nowrap}
.rule{flex:1;border-top:1px solid #999;margin-top:16px}
.address{text-align:right;font-size:11px;color:var(--ink-soft);line-height:1.3;white-space:nowrap}
.contact{display:flex;gap:120px;margin-top:8px;font-size:11px;color:var(--ink-soft)}
.timeline{position:relative;flex:none}
.timeline:before{content:"";position:absolute;left:22px;top:0;bottom:0;border-left:1.5px solid var(--line)}
.section{position:relative;padding:9px 30px 9px 42px}
.section.shaded{background:var(--band)}
.section.accent{box-shadow:inset -8px 0 0 var(--blue)}
.section-title{font-family:"EB Garamond",serif;font-size:14px;line-height:18px;letter-spacing:1.2px;text-transform:uppercase;font-weight:500;color:var(--ink);margin-bottom:4px}
.dot{position:absolute;left:15px;top:11px;width:15px;height:15px;border-radius:50%;background:var(--blue)}
.profile p{color:var(--ink-soft)}
.edu{display:flex;gap:40px}
.edu-item{flex:1}
.edu-item .school:before{content:"";display:inline-block;width:5px;height:5px;border-radius:50%;background:var(--ink);margin-right:7px;vertical-align:middle}
.edu-item .indent{padding-left:12px;color:var(--ink-soft)}
.edu-item .degree{padding-left:12px;margin-top:5px;color:var(--ink-soft)}
.edu-item .degree:before{content:"";display:inline-block;width:20px;border-top:1px solid #888;margin-right:6px;vertical-align:middle}
.edu-item .major{padding-left:38px;color:var(--ink-soft)}
.quals{display:grid;grid-template-columns:1.5fr 1.1fr 1fr;gap:0 14px;font-size:10.5px}
.quals ul{list-style:none}
.quals li{padding-left:13px;position:relative;white-space:nowrap}
.quals .left li:before{content:"";position:absolute;left:0;top:4px;border:4px solid transparent;border-right:5px solid var(--ink);border-left:0}
.quals .mid li:before{content:"";position:absolute;left:0;top:4px;width:6px;height:7px;border-left:2px solid var(--ink);border-right:2px solid var(--ink)}
.quals .right li:before{content:"";position:absolute;left:0;top:4px;border:4px solid transparent;border-left:5px solid var(--ink);border-right:0}
.job{display:grid;grid-template-columns:170px 1fr;gap:16px;margin-bottom:6px}
.job:last-child{margin-bottom:0}
.job-title{font-weight:700;font-size:10.5px;color:var(--ink);white-space:nowrap}
.job-meta{border-left:1px solid #777;margin-left:4px;padding-left:8px;font-size:9.5px;color:var(--ink-soft)}
.job-desc{color:var(--ink-soft)}
.closing{position:relative;flex:1;margin:0 30px 16px 22px;border:1.5px solid var(--line);border-left:0;display:flex}
.closing-col{flex:1;position:relative;padding:16px 10px 0 22px}
.closing-col .dot{left:-7px;top:-8px}
.closing-col ul{list-style:none;font-size:10.5px}
.closing-col li{padding-left:12px;position:relative;margin-bottom:2px}
.closing-col li:before{content:"";position:absolute;left:0;top:5px;width:5px;height:5px;border-radius:50%;background:var(--ink)}
.seal{position:absolute;right:-8px;bottom:-8px;width:30px;height:30px;border-radius:50%;background:var(--blue);border:2px solid #fff;box-shadow:0 0 0 1px var(--blue)}
</style>
</head>
<body>
<main class="resume">
  <div class="top-bar"><div class="grey"></div><div class="blue"></div></div>

  <header class="masthead">
    <div class="masthead-row">
      <h1 class="name">Tobias Garrick Elwin III</h1>
      <div class="rule"></div>
      <div class="address">218 Larkspur Lane<br>Atlanta, Georgia 30318</div>
    </div>
    <div class="contact"><span>404-555-0186</span><span>tgelwin@mailbox.example</span></div>
  </header>

  <div class="timeline">
    <section class="section profile accent">
      <span class="dot"></span>
      <h2 class="section-title">Profile</h2>
      <p>Recent graduate of a highly ranked university seeking opportunities to apply composition and production talents across a variety of music genres and other media. Expertise lies in delivering high quality sound design, editing, mixing, and recording. Excellent interpersonal skills and the ability to build strong relationships with people at all levels. Exceptionally motivated self-starter and creative problem solver who enjoys working collaboratively on teams.</p>
    </section>

    <section class="section shaded">
      <span class="dot"></span>
      <h2 class="section-title">Education</h2>
      <div class="edu">
        <div class="edu-item">
          <div class="school">Coral Bay University – Halvorsen School of Music</div>
          <div class="indent">Coral Springs, Florida</div>
          <div class="degree">Bachelor of Music – May 2016</div>
          <div class="major">Major: Media Writing and Production, GPA 3.20/4.0</div>
        </div>
        <div class="edu-item">
          <div class="school">Briarwood Academy</div>
          <div class="indent">College Park, Georgia</div>
          <div class="degree">High School Diploma with Honors – May 2011</div>
        </div>
      </div>
    </section>

    <section class="section accent">
      <span class="dot"></span>
      <h2 class="section-title">Highlights of Qualifications</h2>
      <div class="quals">
        <ul class="left">
          <li>Media Production Software (SessionDesk 11)</li>
          <li>Sound Design</li>
          <li>Sound Acoustics</li>
          <li>Studio Recording</li>
          <li>Audio Editing</li>
        </ul>
        <ul class="mid">
          <li>Audio Mixing</li>
          <li>Analog/Digital board operation</li>
          <li>Music Arranging</li>
          <li>Music Composition</li>
          <li>Music Production</li>
        </ul>
        <ul class="right">
          <li>Composing Sheet Music</li>
          <li>Singer-songwriter</li>
          <li>Rhythm guitarist</li>
        </ul>
      </div>
    </section>

    <section class="section shaded">
      <span class="dot"></span>
      <h2 class="section-title">Work Experience</h2>
      <div class="job">
        <div><div class="job-title">Sound Engineer</div><div class="job-meta">Palmetto Picture House (PPH)<br>Miami, FL<br>May 2014 – Present</div></div>
        <p class="job-desc">Edited and mixed recorded field audio to professional standards. Matched audio with motion picture video to create a seamless product. Recorded automated dialogue replacement (ADR) audio and integrated into motion picture video project using SessionDesk 11. Recorded foley sound effects to be added to film, video, and other media in post-production. Composed and recorded original music to accompany various video projects.</p>
      </div>
      <div class="job">
        <div><div class="job-title">Sales Associate</div><div class="job-meta">Northline Retail Corporation<br>Atlanta, GA<br>May 2013 – October 2013</div></div>
        <p class="job-desc">Provided customer service, maintained a clean and organized work environment, assisted in sales, and performed cashier responsibilities.</p>
      </div>
      <div class="job">
        <div><div class="job-title">On-Site Promoter/Intern</div><div class="job-meta">Georgia CAL<br>(Civic Action League)<br>Atlanta, GA<br>June 2012 – August 2012</div></div>
        <p class="job-desc">Promoted and advertised various campaigns and managed various office tasks, such as setting up site maps and organizing and sorting non-profit donations.</p>
      </div>
      <div class="job">
        <div><div class="job-title">Product Marketing Consultant</div><div class="job-meta">Meridian Direct Sales, Inc.<br>Atlanta, GA<br>June 2011 – August 2011</div></div>
        <p class="job-desc">Conducted direct sales and marketing of subsidiary product line through establishing a compelling value proposition, overcoming objections, and closing the sale.</p>
      </div>
    </section>
  </div>

  <div class="closing">
    <section class="closing-col">
      <span class="dot"></span>
      <h2 class="section-title">Honors/Awards</h2>
      <ul>
        <li>Best Film and Score: Frights and Frames 2015 Competition (Coral Bay University)</li>
        <li>Harold B Winslow Scholar</li>
        <li>Best New Member, Delta Tau Omega Fraternity, Inc.</li>
        <li>Coral Bay University Homecoming King, 2012</li>
      </ul>
    </section>
    <section class="closing-col">
      <span class="dot"></span>
      <h2 class="section-title">Professional Affiliations</h2>
      <ul>
        <li>Member, Guild of Contemporary Composers (GCC)</li>
        <li>Member, National Alliance of Songwriters, Authors and Publishers (NASAP)</li>
        <li>Member, Sound Craft Society (SCS)</li>
        <li>Member, Delta Tau Omega Fraternity, Incorporated</li>
      </ul>
    </section>
    <span class="seal"></span>
  </div>
</main>
</body>
</html>
```